Business Cards Needed

Hi designers, I have a new logo that was created by one of the ArtMingle designers. I'd now like to use that logo to make business cards. The company is called VitaLumen Advisors and is a business consulting firm. I'd like the business cards to be horizontal, modern, and professional.
I'd like the following information to be on the business card:
1) Logo
2) my name - Marisa Kolvane
3) my title - Principal
4) name of business - VitaLumen Advisors
5) mobile - 508.372.9146
6) e-mail - marisa@vitalumenadvisors.example
I'm uploading a JPG file of the logo. I'm hoping this is the correct file format. Please let me know if you need another type of file. Thank you.
Look and feel
Each slider illustrates characteristics of the customer's brand and the style your logo design should communicate.

```html
<!DOCTYPE html>
<html lang="en">
<head>
<meta charset="utf-8">
<title>VitaLumen Advisors – Business Card</title>
<link rel="stylesheet" href="https://fonts.googleapis.com/css2?family=Cinzel:wght@400&family=Montserrat:wght@500;700;800&family=Arimo:wght@400&display=swap">
<style>
  :root {
    --backdrop: #353334;
    --card: #e6e7e8;
    --teal-dark: #1a727a;
    --teal-mid: #3c9199;
    --teal-light: #52a8b1;
    --brand-blue: #1275bb;
    --white: #ffffff;
  }
  html, body {
    margin: 0;
    padding: 0;
    width: 1200px;
    height: 1200px;
    overflow: hidden;
    background: var(--backdrop);
  }
  .card {
    position: absolute;
    left: 212px;
    width: 776px;
    height: 411px;
    display: block;
  }
  .card--front { top: 173px; }
  .card--back { top: 615px; }
  .card-base { fill: var(--card); }
  .tone-start { stop-color: var(--teal-light); }
  .tone-mid { stop-color: var(--teal-mid); }
  .tone-end { stop-color: var(--teal-dark); }
  .brand-name {
    font-family: "Montserrat", sans-serif;
    font-weight: 500;
    font-size: 62px;
    fill: var(--brand-blue);
  }
  .holder-name {
    font-family: "Cinzel", serif;
    font-weight: 400;
    font-size: 72px;
    fill: var(--white);
  }
  .name-rule { stroke: var(--white); stroke-width: 5; }
  .holder-title {
    font-family: "Montserrat", sans-serif;
    font-weight: 800;
    font-size: 46px;
    fill: var(--white);
  }
  .contact-phone {
    font-family: "Arimo", sans-serif;
    font-size: 47px;
    fill: var(--white);
  }
  .contact-email {
    font-family: "Montserrat", sans-serif;
    font-weight: 700;
    font-size: 24px;
    fill: var(--white);
  }
  .icon-fill { fill: var(--white); }
  .icon-line { fill: none; stroke: var(--white); stroke-width: 3; stroke-linejoin: round; }
</style>
</head>
<body>

<svg class="card card--front" viewBox="0 0 1249 662" aria-label="Card front">
  <defs>
    <linearGradient id="front-band-tone" x1="0" y1="0" x2="0" y2="1">
      <stop offset="0" class="tone-start"/>
      <stop offset="0.45" class="tone-mid"/>
      <stop offset="1" class="tone-end"/>
    </linearGradient>
  </defs>
  <rect class="card-base" width="1249" height="662"/>
  <text class="brand-name" x="625" y="282" text-anchor="middle">VitaLumen Advisors</text>
  <rect class="front-band" x="0" y="440" width="1249" height="222" fill="url(#front-band-tone)" role="img" aria-label="Decorative teal wave band"/>
</svg>

<svg class="card card--back" viewBox="0 0 1249 661" aria-label="Card back">
  <defs>
    <linearGradient id="back-panel-tone" x1="0" y1="0" x2="1" y2="0">
      <stop offset="0" class="tone-end"/>
      <stop offset="0.8" class="tone-end"/>
      <stop offset="1" class="tone-mid"/>
    </linearGradient>
  </defs>
  <rect class="card-base" width="1249" height="661"/>
  <rect class="back-panel" x="0" y="0" width="680" height="661" fill="url(#back-panel-tone)" role="img" aria-label="Decorative teal wave panel"/>

  <text class="holder-name" x="30" y="78" textLength="618" lengthAdjust="spacingAndGlyphs">MARISA KOLVANE</text>
  <line class="name-rule" x1="31" y1="93" x2="648" y2="93"/>
  <text class="holder-title" x="29" y="140">PRINCIPAL</text>

  <g class="contact-row contact-row--phone">
    <path class="icon-fill" d="M42,205 C48,201 54,207 57,213 C59,217 52,221 54,226 C60,238 72,248 84,254 C89,256 92,249 97,251 C103,254 110,258 106,264 C100,271 92,273 84,270 C62,262 43,244 34,224 C31,216 35,209 42,205 Z"/>
    <text class="contact-phone" x="143" y="272">508.372.9146</text>
  </g>

  <g class="contact-row contact-row--email">
    <rect class="icon-line" x="32" y="308" width="74" height="58" rx="9"/>
    <rect class="icon-line" x="38" y="314" width="62" height="46" rx="6"/>
    <polyline class="icon-line" points="46,354 46,324 69,340 92,324 92,354"/>
    <text class="contact-email" x="143" y="342">marisa@vitalumenadvisors.example</text>
  </g>
</svg>

</body>
</html>
```